Business Cards for Logistics Company

Looking to update Business Card Design.
Logo is attached. Blue background is not a part of the logo, you can remove it in layers.

Company: Harbor Crest Freightways
Industry: Logistics, Container Shipping

Address:
418 Willow Bend Ave
Bayonne NJ 07419

Phones:
p. 201-555-3142
f. 201-555-3149
c. very by person's name

Website: www.hcfroute.example

Design has to include person's name and position.

Target Market(s)

B2B

Industry/Entity Type

Business

Contact Information for Business Card

Card Size (non standard): 1039 x 697 pixels, 300dpi

Font styles to use
Serif
Sans Serif

```html
<!DOCTYPE html>
<html lang="en">
<head>
<meta charset="utf-8">
<title>Harbor Crest Freightways – Business Cards</title>
<link href="https://fonts.googleapis.com/css2?family=Open+Sans:wght@400;600;700&display=swap" rel="stylesheet">
<style>
  :root {
    --bg-top: #5d6773;
    --bg-bottom: #2c333c;
    --card-dark: #1d1b1c;
    --card-light: #ffffff;
    --brand-blue: #3a78c6;
    --band-blue: #4b80c6;
    --band-grey: #8a8d92;
    --text-grey: #5b5e63;
    --text-light: #f2f2f2;
  }
  * { box-sizing: border-box; margin: 0; padding: 0; }
  html, body { width: 1200px; height: 960px; overflow: hidden; }
  body {
    background: radial-gradient(ellipse at 50% 35%, var(--bg-top), var(--bg-bottom) 80%);
    font-family: "Open Sans", Arial, sans-serif;
    position: relative;
  }
  .card {
    position: absolute;
    left: 300px;
    width: 600px;
    height: 402px;
    box-shadow: 0 14px 30px rgba(0,0,0,.45);
    overflow: hidden;
  }
  .card--back { top: 48px; background: var(--card-dark); }
  .card--front { top: 506px; background: var(--card-light); }

  .brand { display: flex; align-items: center; gap: 16px; }
  .brand__mark { width: 58px; height: 58px; background: var(--brand-blue); flex: none; }
  .brand__name {
    font-weight: 400;
    letter-spacing: 4px;
    text-transform: uppercase;
    line-height: 1.25;
  }

  .card--back .brand { position: absolute; left: 130px; top: 112px; }
  .card--back .brand__name { color: var(--text-light); font-size: 19px; width: 260px; }
  .tagline {
    position: absolute; left: 0; right: 0; top: 246px;
    text-align: center; color: var(--text-light);
  }
  .tagline__title { font-size: 13px; letter-spacing: .5px; }
  .tagline__services { font-size: 13.5px; margin-top: 4px; }

  .card--front .brand { position: absolute; left: 36px; top: 110px; }
  .card--front .brand__name { color: var(--brand-blue); font-size: 15px; width: 210px; }

  .card__art { position: absolute; inset: 0; }

  .contact { position: absolute; left: 322px; top: 78px; right: 24px; color: var(--text-grey); }
  .contact__name { color: var(--brand-blue); font-weight: 700; font-size: 19px; line-height: 1.1; }
  .contact__role { font-size: 13.5px; margin-bottom: 18px; }
  .contact__company { color: var(--brand-blue); font-weight: 600; font-size: 13.5px; }
  .contact__address { font-size: 13px; margin-bottom: 14px; white-space: nowrap; }
  .contact__list { list-style: none; font-size: 13.5px; }
  .contact__list li { display: flex; align-items: center; gap: 10px; height: 21px; }
  .contact__list svg { width: 15px; height: 15px; flex: none; }
</style>
</head>
<body>

<section class="card card--back" aria-label="Card back">
  <div class="brand">
    <span class="brand__mark"></span>
    <span class="brand__name">Harbor Crest Freightways</span>
  </div>
  <div class="tagline">
    <p class="tagline__title">INTERNATIONAL TRANSPORTATION SOLUTIONS</p>
    <p class="tagline__services">Ocean &amp; Air Freight &bull; Loading &amp; Storage &bull; Multimodal Transport</p>
  </div>
</section>

<section class="card card--front" aria-label="Card front">
  <svg class="card__art" viewBox="0 0 600 402" preserveAspectRatio="none" aria-hidden="true">
    <path d="M0 262 C150 330 380 370 600 360 L600 402 L0 402 Z" fill="var(--band-blue)"/>
    <path d="M0 240 C150 300 380 345 600 348 L600 354 C380 356 150 318 0 254 Z" fill="var(--band-grey)"/>
    <line x1="302" y1="50" x2="256" y2="280" stroke="var(--band-grey)" stroke-width="2.5"/>
  </svg>

  <div class="brand">
    <span class="brand__mark"></span>
    <span class="brand__name">Harbor Crest Freightways</span>
  </div>

  <div class="contact">
    <p class="contact__name">Nikolai Barrow</p>
    <p class="contact__role">General Manager</p>
    <p class="contact__company">Harbor Crest Freightways</p>
    <p class="contact__address">418 Willow Bend Ave, Bayonne NJ 07419</p>
    <ul class="contact__list">
      <li><svg viewBox="0 0 16 16"><path d="M2 5c0-2 2-3 6-3s6 1 6 3v1h-3V5H5v1H2z M3 7h10l1 7H2z" fill="var(--brand-blue)"/></svg>(201) 555.3142</li>
      <li><svg viewBox="0 0 16 16"><rect x="4" y="1" width="8" height="5" fill="var(--brand-blue)"/><rect x="1" y="6" width="14" height="6" rx="1" fill="var(--brand-blue)"/><rect x="4" y="10" width="8" height="5" fill="#fff" stroke="var(--brand-blue)"/></svg>(201) 555.3149</li>
      <li><svg viewBox="0 0 16 16"><rect x="4" y="1" width="8" height="14" rx="1.5" fill="none" stroke="var(--brand-blue)" stroke-width="1.5"/></svg>(646) 555.0178</li>
      <li><svg viewBox="0 0 16 16"><rect x="1" y="3" width="14" height="10" fill="none" stroke="var(--brand-blue)" stroke-width="1.3"/><path d="M1 3l7 6 7-6" fill="none" stroke="var(--brand-blue)" stroke-width="1.3"/></svg>info@hcfroute.example</li>
      <li><svg viewBox="0 0 16 16"><circle cx="8" cy="8" r="6.5" fill="none" stroke="var(--brand-blue)" stroke-width="1.3"/><ellipse cx="8" cy="8" rx="3" ry="6.5" fill="none" stroke="var(--brand-blue)"/><path d="M1.5 8h13M2.5 5h11M2.5 11h11" stroke="var(--brand-blue)"/></svg>www.hcfroute.example</li>
    </ul>
  </div>
</section>

</body>
</html>
```